We need a very creative business card for a leading diamond tools manufactures in india

1. Iso 9001:2000
2. Logo
3. Leading Manufacture of stone cutting tools: Gang Saw Segment, Circular Segment, wire saw segment and rubber and plastic coated diamond wire rope.
4. Spirit for success
5. Kalvani Mokesh Diamond Tools Pvt. Ltd.
6. Mo. No. 9817406352
7. Email: Rakesh@kmgroup-tardex.com
8. Web: kmgroup-tardex.com
9.CEO
10. Reg. Office. 47, pushpa vihar , naya basti, dholpura ,dist. Rajsamand (rajasthan) 313587
11.Rakesh Jandal
Our audience are Adult based in english speaking person having age between 25-55 that handle granite and marble business.
Plastic

```html
<!DOCTYPE html>
<html lang="en">
<head>
<meta charset="utf-8">
<title>Business Card – Managing Director</title>
<link rel="stylesheet" href="https://fonts.googleapis.com/css2?family=Jura:wght@500;600;700&display=swap">
<style>
  :root {
    --page-bg: #cfcac3;
    --card-bg: #ebe9e5;
    --card-edge: #d6d3ce;
    --ink: #2f2f2f;
    --ink-soft: #3c3c3c;
    --brand-red: #b3241d;
    --brand-yellow: #f7c600;
    --white: #ffffff;
    --rule: #9a9792;
  }
  * { margin: 0; padding: 0; box-sizing: border-box; }
  html, body {
    width: 1200px;
    height: 768px;
    overflow: hidden;
    background: var(--page-bg);
    font-family: "Jura", sans-serif;
  }
  .card {
    position: absolute;
    left: 150px;
    top: 123px;
    width: 900px;
    height: 522px;
    border-radius: 24px;
    background: var(--card-bg);
    border: 1px solid var(--card-edge);
    overflow: hidden;
    box-shadow: 0 18px 40px rgba(0,0,0,0.18);
    color: var(--ink);
  }
  .brand-mark {
    position: absolute;
    right: 48px;
    top: 108px;
    display: flex;
    align-items: center;
    gap: 12px;
  }
  .brand-mark__dot {
    width: 28px;
    height: 28px;
    border-radius: 50%;
    background: var(--brand-yellow);
  }
  .brand-mark__name {
    font-size: 36px;
    font-weight: 700;
    color: var(--brand-red);
    letter-spacing: 1px;
  }
  .holder__name {
    position: absolute;
    left: 38px;
    top: 168px;
    font-size: 27px;
    font-weight: 600;
    letter-spacing: 1.5px;
  }
  .holder__role {
    position: absolute;
    left: 38px;
    top: 217px;
    font-size: 20px;
    font-weight: 600;
    color: var(--brand-red);
  }
  .divider {
    position: absolute;
    left: 55px;
    top: 258px;
    width: 785px;
    height: 2px;
    background: linear-gradient(90deg, rgba(154,151,146,0) 0%, var(--rule) 30%, var(--rule) 75%, rgba(154,151,146,0) 100%);
  }
  .address {
    position: absolute;
    left: 38px;
    top: 340px;
    font-size: 21px;
    font-style: normal;
    font-weight: 600;
    line-height: 28px;
    color: var(--ink-soft);
    letter-spacing: 0.5px;
  }
  .contacts {
    position: absolute;
    right: 30px;
    top: 268px;
    list-style: none;
    text-align: right;
  }
  .contacts__item {
    display: flex;
    justify-content: flex-end;
    align-items: center;
    gap: 12px;
    font-weight: 600;
    color: var(--ink-soft);
  }
  .contacts__item--phone { font-size: 19px; height: 44px; letter-spacing: 1px; }
  .contacts__item--web { font-size: 17px; height: 30px; }
  .contacts__icon { width: 20px; height: 20px; flex: none; }
  .footer-band {
    position: absolute;
    left: 0;
    bottom: 0;
    width: 900px;
    height: 58px;
  }
  .footer-band__url {
    position: absolute;
    left: 38px;
    bottom: 20px;
    font-size: 18px;
    font-weight: 600;
    color: var(--white);
    letter-spacing: 0.5px;
  }
</style>
</head>
<body>
  <main class="card">
    <div class="brand-mark">
      <span class="brand-mark__dot"></span>
      <span class="brand-mark__name">KM GROUP</span>
    </div>

    <h1 class="holder__name">MARK HOLLOWAY</h1>
    <p class="holder__role">Managing Director</p>
    <div class="divider"></div>

    <address class="address">
      071.12th floor,Plaza<br>Harbour Road PKT
    </address>

    <ul class="contacts">
      <li class="contacts__item contacts__item--phone">098 765 4321
        <svg class="contacts__icon" viewBox="0 0 24 24" fill="#3c3c3c"><path d="M6.6 10.8a15.1 15.1 0 0 0 6.6 6.6l2.2-2.2c.3-.3.7-.4 1-.2 1.1.4 2.3.6 3.6.6.6 0 1 .4 1 1V20c0 .6-.4 1-1 1A17 17 0 0 1 3 4c0-.6.4-1 1-1h3.5c.6 0 1 .4 1 1 0 1.3.2 2.5.6 3.6.1.3 0 .7-.2 1z"/></svg>
      </li>
      <li class="contacts__item contacts__item--phone">098 765 4322
        <svg class="contacts__icon" viewBox="0 0 24 24" fill="none" stroke="#3c3c3c" stroke-width="2.2"><rect x="6.5" y="2" width="11" height="20" rx="2"/><line x1="10" y1="18.5" x2="14" y2="18.5"/></svg>
      </li>
      <li class="contacts__item contacts__item--phone">098 765 4323
        <svg class="contacts__icon" viewBox="0 0 24 24" fill="#3c3c3c"><rect x="3" y="8" width="18" height="13" rx="1.5"/><rect x="7" y="3" width="10" height="6"/><rect x="6" y="11" width="3" height="2" fill="#ebe9e5"/><rect x="11" y="11" width="3" height="2" fill="#ebe9e5"/><rect x="6" y="15" width="3" height="2" fill="#ebe9e5"/><rect x="11" y="15" width="3" height="2" fill="#ebe9e5"/></svg>
      </li>
      <li class="contacts__item contacts__item--web">info@kmgroup.com
        <svg class="contacts__icon" viewBox="0 0 24 24" fill="#3c3c3c"><path d="M2 5h20v14H2z"/><path d="M2 5l10 8 10-8" fill="none" stroke="#ebe9e5" stroke-width="1.8"/></svg>
      </li>
      <li class="contacts__item contacts__item--web">www.kmgrouptools.com
        <svg class="contacts__icon" viewBox="0 0 24 24" fill="none" stroke="#3c3c3c" stroke-width="1.8"><circle cx="12" cy="12" r="9.5"/><ellipse cx="12" cy="12" rx="4" ry="9.5"/><line x1="2.5" y1="12" x2="21.5" y2="12"/><path d="M4.5 7h15M4.5 17h15"/></svg>
      </li>
    </ul>

    <svg class="footer-band" viewBox="0 0 900 58" preserveAspectRatio="none">
      <path d="M0 3 H345 Q362 3 370 20 L388 58 H0 Z" fill="var(--brand-red)"/>
      <path d="M364 20 H900 V58 H388 L380 37 Q374 20 364 20 Z" fill="var(--brand-yellow)"/>
    </svg>
    <span class="footer-band__url">www.kmgrouptools.com</span>
  </main>
</body>
</html>
```